Healthy Vending Machine Business Flyer

A modorn design that represents our healthy vending machine business. We will attach a picture of the machine we want on the flyer along with our logo. We will also upload the wording we want on the flyer

Colors

Designer to choose colors to be used in the design.

Requirements
Must have
• Flyer wording
• Front of flyer:
• (Picture of vending machine on the front)
• Free healthy vending machines hit the Treasure Valley
• Keep your Employees happy & productive with healthy vending options at work
• • No Cost to Your Company
• • Remote tracking tells us when your favorite snacks are running low
• • Credit Card/Smartphone Payment Technology
• • Ability to Customize your Snacks and Drinks
• • Locally Owned and Operated
• • Delicious Healthy Options
• Back of flyer:
• 431 Crispleaf Vending is a locally owned and operated company dedicated to making healthy snacks and drinks easily available for the Treasure Valley. We provide the latest in vending machine technology accepting credit cards, tillo wallet, and norvex wallet. State of the art inventory tracking tells us when your machine is running low so you're never out of your favorite drink or snack. We offer flexible stocking based on your companies needs and work with you on what items you want in the machine. Our goal is to give your employees and clients healthy options on the go
• To be considered for this FREE service for your business please visit: 431crispleafvending.com
• Or call/email today:
• Phone: 431-555-0162
• Email: 431crispleafvending@mailtrove.com
Should not have
• Any Additional Fruit images besides what is on the machine image.

```html
<!DOCTYPE html>
<html lang="en">
<head>
<meta charset="utf-8">
<title>431 Crispleaf Vending – Flyer</title>
<link href="https://fonts.googleapis.com/css2?family=Lato:ital,wght@0,400;0,700;0,900;1,400;1,700&display=swap" rel="stylesheet">
<style>
:root{
  --orange:#f26a0c;
  --orange-light:#f99d1b;
  --yellow:#ffc20e;
  --green:#6db52a;
  --green-dark:#3e8e1d;
  --lime:#9dcc3c;
  --ink:#222;
  --grey-text:#6b6b6b;
  --white:#fff;
}
*{box-sizing:border-box;margin:0;padding:0}
html,body{width:1200px;height:1200px;overflow:hidden}
body{background:linear-gradient(180deg,#c7c7c7,#a9a9a9);font-family:'Lato',sans-serif;position:relative}
.flyer{position:absolute;overflow:hidden;box-shadow:0 6px 18px rgba(0,0,0,.35);background:var(--white)}
.front{left:45px;top:68px;width:545px;height:772px}
.back{left:618px;top:256px;width:549px;height:777px}

/* shared */
.brand{position:absolute;display:flex;align-items:center;gap:10px;color:var(--orange);font-weight:900;font-size:28px;line-height:30px;white-space:nowrap}
.brand-mark{width:22px;height:22px;background:var(--green);flex:none}
.pill{position:absolute;height:29px;border:3px solid var(--white);border-radius:15px;background:var(--orange);color:var(--white);font-weight:700;font-size:15px;display:flex;align-items:center;justify-content:center;gap:8px;white-space:nowrap}
.contact{position:absolute;color:var(--white);font-weight:700;font-size:13px;line-height:17px;white-space:nowrap}
.contact div{display:flex;align-items:center;gap:6px}
.photo{position:absolute}

/* front */
.front .orange-col{position:absolute;left:273px;top:0;width:272px;height:772px;background:linear-gradient(180deg,var(--orange) 0%,var(--orange-light) 70%,var(--yellow) 100%)}
.front .brand{left:26px;top:84px}
.free-band{position:absolute;left:0;top:154px;width:288px;height:60px;background:var(--lime);color:var(--white);font-weight:900;font-size:50px;letter-spacing:1px;display:flex;align-items:center;justify-content:center;padding-right:15px}
.free-fold{position:absolute;left:273px;top:214px;width:0;height:0;border-left:15px solid #4f8d1b;border-bottom:12px solid transparent}
.headline{position:absolute;left:0;width:273px;text-align:center}
.hl-healthy{top:218px;color:var(--orange);font-weight:900;font-size:41px}
.hl-machines{top:264px;color:var(--green-dark);font-weight:900;font-size:22px;letter-spacing:.2px}
.hl-valley{top:292px;color:var(--green);font-weight:700;font-size:20px;border-top:2px solid var(--lime);margin:0 20px;width:233px}
.hl-pitch{top:321px;color:var(--grey-text);font-style:italic;font-size:17px;line-height:21px}
.front .people{left:0;top:420px;width:273px;height:280px;background:linear-gradient(180deg,#e9ecef 0%,#c9cfd6 50%,#8a8f96 100%)}
.front .machine{left:315px;top:362px;width:190px;height:320px;background:linear-gradient(135deg,#2a2a2a 0%,#5b8a2a 45%,#c73a1e 100%);border-radius:3px}
.benefits{position:absolute;left:305px;top:23px;list-style:none}
.benefits li{display:flex;align-items:center;gap:12px;color:var(--white);font-size:13px;line-height:17px;position:absolute;left:0;width:230px}
.icon{width:42px;height:42px;border-radius:50%;background:var(--green);border:3px solid var(--white);flex:none;display:flex;align-items:center;justify-content:center}
.front .pill{left:292px;top:726px;width:253px}
.front .contact{left:24px;top:720px}

/* back */
.back .brand{left:20px;top:100px}
.intro{position:absolute;left:19px;top:167px;width:240px;color:var(--orange);font-style:italic;font-size:15.5px;line-height:20px}
.back .scene{left:262px;top:48px;width:262px;height:262px;border-radius:50%;border:6px solid var(--yellow);background:linear-gradient(135deg,#e5e6e8,#9ea3a8 60%,#5b5f63)}
.pay{position:absolute;width:46px;height:46px;border-radius:50%;background:var(--orange);border:3px solid var(--white);color:var(--white);font-size:10px;font-weight:700;display:flex;align-items:center;justify-content:center;text-align:center;line-height:11px}
.checks{position:absolute;left:64px;top:398px;width:480px;list-style:none}
.checks li{display:flex;gap:10px;color:var(--ink);font-size:14px;line-height:18px;margin-bottom:8px}
.checks b{font-weight:700}
.tick{width:26px;height:26px;flex:none;margin-top:4px}
.goal{position:absolute;left:101px;top:530px;color:var(--white);font-style:italic;font-weight:700;font-size:21px;line-height:28px}
.goal span{color:var(--orange);text-decoration:underline}
.consider{position:absolute;left:264px;top:612px;width:280px;color:var(--ink);font-style:italic;font-size:14px;line-height:18px}
.consider span{color:var(--orange);font-weight:700}
.social{position:absolute;width:60px;height:60px;border-radius:50%;background:var(--green);border:4px solid var(--white);box-shadow:0 0 0 2px var(--green);color:var(--white);font-size:10px;font-weight:700;display:flex;align-items:center;justify-content:center}
.call{position:absolute;left:52px;top:702px;color:var(--white);font-style:italic;font-size:14px}
.back .contact{left:30px;top:727px}
.back .pill{left:284px;top:733px;width:265px}
</style>
</head>
<body>

<section class="flyer front">
  <div class="orange-col"></div>
  <svg width="545" height="772" style="position:absolute;left:0;top:0">
    <defs><linearGradient id="frontGreen" x1="0" x2="1"><stop offset="0" stop-color="#6db52a"/><stop offset="1" stop-color="#b7d532"/></linearGradient></defs>
    <path d="M0,700 C150,665 400,665 545,715 L545,772 L0,772 Z" fill="url(#frontGreen)"/>
    <path d="M0,700 C150,665 400,665 545,715" fill="none" stroke="#fff" stroke-width="5"/>
  </svg>

  <div class="brand"><span class="brand-mark"></span><span>431 Crispleaf<br>Vending</span></div>
  <div class="free-band">FREE</div>
  <div class="free-fold"></div>
  <div class="headline hl-healthy">Healthy</div>
  <div class="headline hl-machines">VENDING MACHINES</div>
  <div class="headline hl-valley">Hit The Treasure Valley</div>
  <div class="headline hl-pitch">Keep your Employees<br>happy &amp; productive with<br>healthy vending options<br>at work</div>

  <div class="photo people" role="img" aria-label="Photo of three cheering office employees"></div>
  <div class="photo machine" role="img" aria-label="Photo of the healthy snack and drink vending machine"></div>

  <ul class="benefits">
    <li style="top:0"><span class="icon"><svg width="22" height="22" viewBox="0 0 22 22"><text x="11" y="18" text-anchor="middle" font-family="Lato,sans-serif" font-weight="900" font-size="20" fill="#fff">$</text></svg></span>No Cost to Your Company</li>
    <li style="top:44px"><span class="icon"><svg width="24" height="24" viewBox="0 0 24 24" fill="none" stroke="#fff" stroke-width="2"><circle cx="12" cy="12" r="8"/><circle cx="12" cy="12" r="3"/><path d="M12 1v5M12 18v5M1 12h5M18 12h5"/></svg></span>Remote tracking tells us<br>when your favorite snacks<br>are running low</li>
    <li style="top:110px"><span class="icon"><svg width="24" height="24" viewBox="0 0 24 24" fill="none" stroke="#fff" stroke-width="2"><rect x="2" y="6" width="20" height="13" rx="2"/><path d="M2 10h20"/></svg></span>Credit Card/Smartphone<br>Payment Technology</li>
    <li style="top:159px"><span class="icon"><svg width="24" height="24" viewBox="0 0 24 24" fill="#fff"><circle cx="6" cy="6" r="2"/><circle cx="12" cy="6" r="2"/><circle cx="18" cy="6" r="2"/><circle cx="6" cy="12" r="2"/><circle cx="12" cy="12" r="2"/><circle cx="18" cy="12" r="2"/><circle cx="12" cy="18" r="2"/></svg></span>Ability to Customize<br>your Snacks and Drinks</li>
    <li style="top:210px"><span class="icon"><svg width="22" height="24" viewBox="0 0 22 24" fill="none" stroke="#fff" stroke-width="2.2"><path d="M11 22 C4 14 4 11 4 9 a7 7 0 0 1 14 0 c0 2 0 5 -7 13z"/><circle cx="11" cy="9" r="2.5"/></svg></span>Locally Owned and Operated</li>
    <li style="top:262px"><span class="icon"><svg width="24" height="24" viewBox="0 0 24 24" fill="none" stroke="#fff" stroke-width="2"><circle cx="12" cy="12" r="9"/><circle cx="9" cy="10" r="1" fill="#fff"/><circle cx="15" cy="10" r="1" fill="#fff"/><path d="M8 14 q4 4 8 0"/></svg></span>Delicious Healthy Options</li>
  </ul>

  <div class="contact">
    <div><svg width="13" height="13" viewBox="0 0 24 24" fill="#fff"><path d="M6 2l4 4-2 3c1 3 4 6 7 7l3-2 4 4-3 4C10 22 2 14 2 5z"/></svg>431-555-0162</div>
    <div><svg width="13" height="11" viewBox="0 0 24 18" fill="none" stroke="#fff" stroke-width="2"><rect x="1" y="1" width="22" height="16"/><path d="M1 1l11 9 11-9"/></svg>431crispleafvending@mailtrove.com</div>
  </div>
  <div class="pill"><svg width="16" height="16" viewBox="0 0 24 24" fill="none" stroke="#fff" stroke-width="2"><circle cx="12" cy="12" r="10"/><path d="M2 12h20M12 2c4 4 4 16 0 20M12 2c-4 4-4 16 0 20"/></svg>431crispleafvending.com</div>
</section>

<section class="flyer back">
  <svg width="549" height="777" style="position:absolute;left:0;top:0">
    <defs>
      <linearGradient id="backGreen" x1="0" y1="0" x2="1" y2="1"><stop offset="0" stop-color="#3e8e1d"/><stop offset="1" stop-color="#b7d532"/></linearGradient>
      <linearGradient id="backWarm" x1="0" y1="0" x2="0" y2="1"><stop offset="0" stop-color="#f26a0c"/><stop offset="1" stop-color="#ffc20e"/></linearGradient>
    </defs>
    <rect x="0" y="560" width="549" height="217" fill="url(#backWarm)"/>
    <path d="M0,392 C120,320 260,290 320,300 C400,340 480,360 549,330 L549,690 C380,690 150,650 0,580 Z" fill="#f26a0c"/>
    <path d="M0,408 C120,338 260,305 320,315 C400,355 480,375 549,345 L549,680 C380,680 150,640 0,568 Z" fill="url(#backGreen)"/>
    <path d="M0,580 C150,650 380,690 549,690" fill="none" stroke="#fff" stroke-width="4"/>
  </svg>

  <div class="brand"><span class="brand-mark"></span><span>431 Crispleaf<br>Vending</span></div>
  <p class="intro">431 Crispleaf Vending<br>is a locally owned and operated company dedicated to making healthy snacks and drinks easily available for the Treasure Valley.</p>

  <div class="photo scene" role="img" aria-label="Photo of a woman choosing a snack at a vending machine keypad"></div>
  <div class="pay" style="left:394px;top:324px"><svg width="22" height="16" viewBox="0 0 24 18" fill="none" stroke="#fff" stroke-width="2"><rect x="1" y="1" width="22" height="16" rx="2"/><path d="M1 6h22"/></svg></div>
  <div class="pay" style="left:447px;top:313px">tillo</div>
  <div class="pay" style="left:491px;top:281px">norvex</div>

  <ul class="checks">
    <li><svg class="tick" viewBox="0 0 26 26"><rect x="2" y="6" width="18" height="18" fill="none" stroke="#fff" stroke-width="2"/><path d="M6 14l5 5 13-16" fill="none" stroke="#fff" stroke-width="3"/></svg><span>We provide the latest in vending machine technology<br>accepting <b>credit cards, tillo wallet, and norvex wallet.</b></span></li>
    <li><svg class="tick" viewBox="0 0 26 26"><rect x="2" y="6" width="18" height="18" fill="none" stroke="#fff" stroke-width="2"/><path d="M6 14l5 5 13-16" fill="none" stroke="#fff" stroke-width="3"/></svg><span>State of the art <b>inventory tracking</b> tells us when your machine<br>is running low so you're never out of your favorite drink or snack.</span></li>
    <li><svg class="tick" viewBox="0 0 26 26"><rect x="2" y="6" width="18" height="18" fill="none" stroke="#fff" stroke-width="2"/><path d="M6 14l5 5 13-16" fill="none" stroke="#fff" stroke-width="3"/></svg><span>We offer <b>flexible stocking</b> based on your companies needs and<br>work with you on what items you want in the machine.</span></li>
  </ul>
  <p class="goal">Our goal is to give your employees and<br>clients <span>healthy options</span> on the go!</p>
  <p class="consider">To be considered for this <span>FREE</span> service for<br>your business please visit our website:</p>

  <div class="social" style="left:396px;top:656px">Pagebook</div>
  <div class="social" style="left:466px;top:654px">Snapgrid</div>

  <p class="call">Or call/email today:</p>
  <div class="contact">
    <div><svg width="13" height="13" viewBox="0 0 24 24" fill="#fff"><path d="M6 2l4 4-2 3c1 3 4 6 7 7l3-2 4 4-3 4C10 22 2 14 2 5z"/></svg>431-555-0162</div>
    <div><svg width="13" height="11" viewBox="0 0 24 18" fill="none" stroke="#fff" stroke-width="2"><rect x="1" y="1" width="22" height="16"/><path d="M1 1l11 9 11-9"/></svg>431crispleafvending@mailtrove.com</div>
  </div>
  <div class="pill"><svg width="16" height="16" viewBox="0 0 24 24" fill="none" stroke="#fff" stroke-width="2"><circle cx="12" cy="12" r="10"/><path d="M2 12h20M12 2c4 4 4 16 0 20M12 2c-4 4-4 16 0 20"/></svg>431crispleafvending.com</div>
</section>

</body>
</html>
```